Podiatry Clinic needs an A0 poster design

we need an A0 poster design for our clinic frontage to include our logo and a feet theme. it is located either in a frame on a glass wall, or in a freestanding poster holder within a shopping centre.
Our clinic values are integrity, respect, excellence, happiness and fun.
We want to let people know that if your feet fail you, then the rest of you slows down very quickly, so get your feet checked immediately. we deal with kids feet, sporty feet, mature feet.

Target Market(s)

parents with kids

Industry/Entity Type

Medical

Requirements
Must have
• Marlow Stride Clinic Logo
• www.marlowstrideclinic.net
• 7261 8092
• easy to read from a distance
Nice to have
• fun, friendly, inviting, colourful, happy.
Should not have
• cartoon
• ugly
• sad
• not too much text
• no fanciful fonts

```html
<!DOCTYPE html>
<html lang="en">
<head>
<meta charset="utf-8">
<title>Marlow Stride Clinic – Poster</title>
<link href="https://fonts.googleapis.com/css2?family=Raleway:wght@400;500;600;700&display=swap" rel="stylesheet">
<style>
  :root {
    --page-bg: #e6eaee;
    --white: #ffffff;
    --brand-blue: #1e6fbf;
    --sky-blue: #3cb3e6;
    --band-blue: #1c7cc9;
    --panel-blue: rgba(52, 170, 222, 0.92);
    --ink: #1a1a1a;
    --grey-text: #5a6470;
  }
  * { box-sizing: border-box; margin: 0; padding: 0; }
  html, body { width: 1200px; height: 800px; overflow: hidden; }
  body {
    background: var(--page-bg);
    font-family: "Raleway", Arial, sans-serif;
    position: relative;
  }
  .poster {
    position: absolute;
    left: 339px; top: 30px;
    width: 522px; height: 740px;
    background: var(--white);
    box-shadow: 0 6px 24px rgba(0,0,0,0.18);
    overflow: hidden;
  }
  /* Header */
  .header {
    position: absolute; left: 0; top: 0; width: 100%; height: 92px;
    display: flex; align-items: center; padding: 0 14px;
  }
  .brand { display: flex; align-items: center; gap: 8px; width: 232px; }
  .brand-dot {
    width: 46px; height: 46px; border-radius: 50%;
    background: var(--brand-blue); flex-shrink: 0;
  }
  .brand-name {
    font-weight: 600; font-size: 19px; line-height: 1.05;
    color: var(--brand-blue);
  }
  .tagline {
    font-weight: 700; font-size: 18px; line-height: 1.25;
    color: var(--brand-blue); margin-left: 10px;
  }
  /* Hero photo area */
  .hero {
    position: absolute; left: 0; top: 92px; width: 100%; height: 291px;
  }
  .hero-photo {
    position: absolute; inset: 0;
    background: radial-gradient(ellipse at 40% 55%, #e2b6b4 0%, #c99a9c 35%, #8d8c93 75%, #6f7480 100%);
  }
  .hero-wedge { position: absolute; inset: 0; }
  .hero-copy {
    position: absolute; right: 8px; bottom: 12px; width: 290px;
    text-align: right; color: var(--white);
  }
  .hero-title { font-weight: 600; font-size: 28px; letter-spacing: 0.3px; margin-bottom: 6px; }
  .hero-text { font-size: 13px; line-height: 1.28; font-weight: 500; }
  .divider-band {
    position: absolute; left: 0; top: 383px; width: 100%; height: 17px;
    background: var(--band-blue);
  }
  /* Lower section */
  .lower {
    position: absolute; left: 0; top: 400px; width: 100%; height: 261px;
  }
  .kids-photo {
    position: absolute; left: 0; top: 0; width: 100%; height: 100%;
    background: linear-gradient(180deg, #bfe3f5 0%, #cfe8c9 45%, #d8b83a 62%, #5f9b3a 85%, #3f7f2a 100%);
  }
  .info-panel {
    position: absolute; left: 0; top: 0; width: 226px; height: 100%;
    background: var(--panel-blue); color: var(--white);
    padding: 14px 10px 0 14px;
  }
  .info-text { font-size: 12.5px; line-height: 1.32; font-weight: 500; }
  .info-web { margin-top: 40px; font-size: 16.5px; font-weight: 600; line-height: 1.28; }
  /* Footer */
  .footer {
    position: absolute; left: 0; top: 661px; width: 100%; height: 79px;
    display: flex; align-items: center; justify-content: space-between;
    padding: 0 8px 0 14px;
  }
  .contact { display: flex; align-items: center; gap: 8px; font-weight: 700; font-size: 12px; color: var(--ink); }
  .contact svg { flex-shrink: 0; }
</style>
</head>
<body>
  <main class="poster">
    <header class="header">
      <div class="brand">
        <span class="brand-dot"></span>
        <span class="brand-name">Marlow Stride Clinic</span>
      </div>
      <p class="tagline">"The greatest gifts in life<br>are those we give to others"</p>
    </header>

    <section class="hero">
      <div class="hero-photo" role="img" aria-label="Close-up photo of a baby's bare feet"></div>
      <svg class="hero-wedge" width="522" height="291" viewBox="0 0 522 291" aria-hidden="true">
        <polygon points="466,0 522,0 522,291 236,291" fill="#3cb3e6" opacity="0.95"/>
      </svg>
      <div class="hero-copy">
        <h1 class="hero-title">WE FIX FEET!</h1>
        <p class="hero-text">Marlow Stride Clinic is very proud to<br>be recognise as one of perth's<br>leading Family and Sports Podiatry<br>practices</p>
      </div>
    </section>

    <div class="divider-band"></div>

    <section class="lower">
      <div class="kids-photo" role="img" aria-label="Photo of four smiling children sitting barefoot on grass"></div>
      <div class="info-panel">
        <p class="info-text">Marlow Stride Clinic offers complete podiatry services for the entire family, from children, the elderly, athletes and sports enthusiasts, to diabetics and high risk feet.</p>
        <p class="info-web">visit our website at:<br>www.marlowstrideclinic.net<br>to get more info</p>
      </div>
    </section>

    <footer class="footer">
      <div class="contact">
        <svg width="38" height="38" viewBox="0 0 38 38" aria-hidden="true">
          <circle cx="19" cy="19" r="18" fill="#111"/>
          <path d="M12 11c1-1 3-1 4 0l2 3c.6 1 .3 2-.5 2.7l-1 .8c1 2.3 2.7 4 5 5l.8-1c.7-.8 1.7-1.1 2.7-.5l3 2c1 1 1 3 0 4-2 2-5 2-8 0-4-2.5-7-5.5-9-9.5-1.5-3-1-5 1-6.5z" fill="#fff"/>
        </svg>
        <span>08 7261 8092</span>
      </div>
      <div class="contact">
        <svg width="36" height="32" viewBox="0 0 36 32" aria-hidden="true">
          <rect x="1" y="9" width="7" height="22" rx="2" fill="#111"/>
          <rect x="10" y="12" width="25" height="19" rx="2" fill="#111"/>
          <rect x="14" y="1" width="16" height="11" fill="#111"/>
          <rect x="16" y="3" width="12" height="2" fill="#fff"/>
          <rect x="16" y="7" width="12" height="2" fill="#fff"/>
          <rect x="14" y="16" width="17" height="3" fill="#fff"/>
          <rect x="14" y="22" width="4" height="3" fill="#fff"/>
          <rect x="20" y="22" width="4" height="3" fill="#fff"/>
          <rect x="26" y="22" width="4" height="3" fill="#fff"/>
        </svg>
        <span>08 5172 4406</span>
      </div>
      <div class="contact">
        <svg width="40" height="28" viewBox="0 0 40 28" aria-hidden="true">
          <rect x="1" y="1" width="38" height="26" fill="#111"/>
          <path d="M3 3l17 13L37 3M3 25l13-11M37 25L24 14" stroke="#fff" stroke-width="2" fill="none"/>
        </svg>
        <span>info@marlowstrideclinic.net</span>
      </div>
    </footer>
  </main>
</body>
</html>
```